Business Card & Logo Design for a communications based company

I am looking for a business card and logo design for a communications based company.. We specialize in Fiber Optics
I have an image i would like to use towards the logo which i have uploaded. (Use of the image is totally up to you the designers)
Background color - Blue OR Black. (thats just my preference..Use of those colors are totally up to the designer)
Text -
Company Name - Brisa Networks LTD
Name - Marcel Dostiwana
Contact Number - (555) 417-2904
Adress - Palmview Heights
Company Motto - Stay Connected !
Services Offered
Fiber Optic Solutions
Full Networking Solutions
IP Surveillance Systems
Access Control Systems
Alarms
Industry/Entity Type
Communications
Contact Information for Business Card
Text -
Name - Marcel Dostiwana
Adress - Palmview Heights
Services Offered
Fiber Optic Solutions
Full Networking Solutions
IP Surveillance Systems
Access Control Systems
Alarms

```html
<!DOCTYPE html>
<html lang="en">
<head>
<meta charset="utf-8">
<title>Brisa Networks LTD – Business Card</title>
<link rel="stylesheet" href="https://fonts.googleapis.com/css2?family=Tinos:wght@400;700&display=swap">
<style>
  :root {
    --page: #d9d6d0;
    --card: #050608;
    --fiber-deep: #0a1a3a;
    --fiber-mid: #16356f;
    --fiber-light: #2f5fa8;
    --text: #ffffff;
    --text-soft: #c9d3e2;
    --accent: #3fa9d6;
    --globe: #2d7fc4;
  }
  * { box-sizing: border-box; margin: 0; padding: 0; }
  html, body { width: 1200px; height: 892px; overflow: hidden; }
  body {
    background: var(--page);
    font-family: "Tinos", "Times New Roman", serif;
    color: var(--text);
    position: relative;
  }
  .card {
    position: absolute;
    left: 240px;
    width: 720px;
    height: 412px;
    background: var(--card);
    border-radius: 4px;
    overflow: hidden;
    box-shadow: 0 8px 24px rgba(0,0,0,.25);
  }
  .card--front { top: 22px; }
  .card--back { top: 458px; }

  .fiber-photo {
    position: absolute;
    top: 0; bottom: 0;
    background:
      radial-gradient(ellipse at 55% 45%, var(--fiber-light) 0%, var(--fiber-mid) 35%, var(--fiber-deep) 65%, transparent 90%);
  }
  .card--front .fiber-photo { left: 250px; right: -40px; }
  .card--back .fiber-photo { left: -60px; width: 470px; }

  .brand {
    position: absolute;
    display: flex;
    align-items: center;
    gap: 22px;
  }
  .brand__mark {
    width: 112px; height: 112px;
    border-radius: 50%;
    background: var(--globe);
    flex: none;
  }
  .brand__name {
    font-size: 40px;
    font-weight: 700;
    line-height: 1.05;
    color: var(--text);
    white-space: nowrap;
  }
  .brand__tagline {
    margin-top: 8px;
    font-size: 20px;
    color: var(--text);
  }
  .card--front .brand { left: 40px; top: 48px; }
  .card--back .brand {
    right: 40px;
    top: 48px;
    flex-direction: column;
    align-items: flex-end;
    gap: 16px;
    text-align: right;
  }

  .contact {
    position: absolute;
    left: 176px;
    top: 214px;
  }
  .contact__name { font-size: 28px; }
  .contact__role { font-size: 15px; color: var(--text-soft); margin-bottom: 18px; }
  .contact__row {
    display: flex; align-items: center; gap: 14px;
    font-size: 22px; margin-top: 10px;
  }
  .icon {
    width: 22px; height: 22px;
    background: var(--accent);
    border-radius: 4px;
    display: flex; align-items: center; justify-content: center;
    flex: none;
  }
  .services {
    position: absolute;
    left: 56px;
    top: 196px;
    list-style: none;
    font-size: 19px;
    line-height: 1.75;
    color: var(--text);
  }
</style>
</head>
<body>

<section class="card card--front">
  <div class="fiber-photo" role="img" aria-label="Blue fiber optic strands with glowing bokeh lights"></div>
  <div class="brand">
    <div class="brand__mark"></div>
    <div>
      <div class="brand__name">Brisa Networks LTD</div>
      <div class="brand__tagline">Stay Connected !</div>
    </div>
  </div>
  <div class="contact">
    <div class="contact__name">Marcel Dostiwana</div>
    <div class="contact__role">Managing Director</div>
    <div class="contact__row">
      <span class="icon">
        <svg width="14" height="14" viewBox="0 0 24 24"><path fill="#fff" d="M6.6 10.8a15 15 0 0 0 6.6 6.6l2.2-2.2a1 1 0 0 1 1-.25 11.4 11.4 0 0 0 3.6.57 1 1 0 0 1 1 1V20a1 1 0 0 1-1 1A17 17 0 0 1 3 4a1 1 0 0 1 1-1h3.5a1 1 0 0 1 1 1c0 1.25.2 2.45.57 3.57a1 1 0 0 1-.25 1z"/></svg>
      </span>
      (555) 417-2904
    </div>
    <div class="contact__row">
      <span class="icon">
        <svg width="14" height="14" viewBox="0 0 24 24"><path fill="#fff" d="M12 2a7 7 0 0 0-7 7c0 5 7 13 7 13s7-8 7-13a7 7 0 0 0-7-7zm0 9.5A2.5 2.5 0 1 1 12 6.5a2.5 2.5 0 0 1 0 5z"/></svg>
      </span>
      Palmview Heights
    </div>
  </div>
</section>

<section class="card card--back">
  <div class="fiber-photo" role="img" aria-label="Blue fiber optic strands with glowing bokeh lights"></div>
  <ul class="services">
    <li>Fiber Optic Solutions</li>
    <li>Full Networking Solutions</li>
    <li>IP Surveillance Systems</li>
    <li>Access Control Systems</li>
    <li>Alarms</li>
  </ul>
  <div class="brand">
    <div class="brand__name">Brisa Networks LTD</div>
    <div class="brand__mark"></div>
  </div>
</section>

</body>
</html>
```